Calloway Brewhouse Beer Can Design

Design a beer can for a boutique craft brewery located in Frankston, Victoria, AUS.
We have a focus on producing socially approachable beers in an ambient setting. The beer can design should be sophisticated, simple, recognizable and a little playful. The color pallet should be inviting and not too bold. The design should have identifying features that can be interchanged onto different cans for different beer types. The design must be repeatable for other beer varieties, which will each have a unique color. The can should feature black, white and purple (this should be in interchangeable color). The beer can also needs to have our Calloway Brewhouse company logo on it, this has been attached to the design brief.

Target Market(s)

The target market is aged 25+ who are social, have some disposable income and appreciate good beer, wine and food.
The beers will also be made for distribution, initially to locally to restaurants and cafés and eventually commercially.
Tourists will also be targeted due to the area the brewhouse is located (Mornington Peninsula, Victoria, AUS).

Industry/Entity Type

Hospitality

Font styles to use
Sans Serif
Script

Colors
6b449b
876aae
b7a5cd
e4daeb
000000
ffffff
959595

Requirements
Must have
• The ‘Calloway Brewhouse’ logo.
• The colour associated to this beer - purple. This should be the only colour used on the can (along with black/white/gray).
• The company tagline ‘Socially Approachable’.
• The tasting notes text ‘Bright in colour, dry on the palate and thirst quenching in the extreme, wheat and pale malts compliment each other with nuance.’
• Australian beer can requirements as per 'Requirements.png'. EPS and AI files of the requirements have been included.
Nice to have
• The logo text ‘Wendel Malt IPA’ more predominant than the Calloway Brewhouse logo.
Should not have
• Be busy, simple is best
• Beer related pictures / images
• Bold, masculine lines and fonts
• Requirements.png directly used. Please use the EPS or AI files provided.

```html
<!DOCTYPE html>
<html lang="en">
<head>
<meta charset="utf-8">
<title>Calloway Brewhouse – Wendel Malt IPA can label</title>
<link href="https://fonts.googleapis.com/css2?family=Allura&family=Bebas+Neue&family=Oswald:wght@400;500&display=swap" rel="stylesheet">
<style>
  :root{
    --purple-deep:#6b449b;
    --purple-mid:#876aae;
    --purple:#b7a5cd;
    --band-grey:#e6e7e9;
    --black:#000000;
    --white:#ffffff;
    --grey:#959595;
    --guide:#5ec8f0;
    --script:"Allura", cursive;
    --display:"Bebas Neue", sans-serif;
    --sans:"Oswald", sans-serif;
  }
  *{box-sizing:border-box;margin:0;padding:0}
  html,body{width:1200px;height:927px;overflow:hidden;background:var(--white)}
  .canvas{position:relative;width:1200px;height:927px}

  .can-label{position:absolute;left:150px;top:228px;width:888px;height:462px;background:var(--purple);overflow:hidden;color:var(--white)}
  .can-label p,.can-label h1,.can-label h2{position:absolute;white-space:nowrap}
  .header-band{position:absolute;left:0;top:12px;width:100%;height:140px;background:var(--band-grey)}
  .wave{position:absolute;left:0;top:0;width:888px;height:462px}

  .bleed-guide{position:absolute;top:228px;height:462px;width:1px;background:var(--guide)}
  .bleed-top{position:absolute;left:150px;top:228px;width:888px;height:1px;background:var(--guide)}
  .bleed-bottom{position:absolute;left:150px;top:689px;width:888px;height:1px;background:var(--guide)}

  .tagline-header{left:57px;top:96px;font-family:var(--script);font-size:27px;line-height:36px;color:var(--black)}

  .brand-name{left:330px;top:52px;width:230px;text-align:center;font-family:var(--sans);font-weight:400;color:var(--black);font-size:26px;line-height:34px;letter-spacing:4px}

  .origin-stamp{position:absolute;left:573px;top:93px;width:102px;height:102px;border:2px solid var(--black);border-radius:50%}

  .side-title{left:28px;top:186px;width:280px;text-align:center;font-family:var(--display);font-size:36px;line-height:36px;letter-spacing:1px}
  .side-rule{position:absolute;left:78px;top:230px;width:180px;height:1px;background:var(--white)}
  .tasting-notes{left:68px;top:244px;width:200px;white-space:normal !important;text-align:center;font-family:var(--display);font-size:10.5px;line-height:13px;letter-spacing:1px}
  .member-badge{position:absolute;left:134px;top:315px;width:68px;height:50px;border:2px solid var(--white)}
  .brewed-at{left:28px;top:383px;width:280px;text-align:center;font-family:var(--sans);font-size:12px;line-height:12px}
  .made-in{left:28px;top:414px;width:280px;text-align:center;font-family:var(--sans);font-size:8.5px;line-height:10px;letter-spacing:.5px}
  .side-abv{left:28px;top:433px;width:280px;text-align:center;font-family:var(--sans);font-size:13px;line-height:16px}

  .hero-name{left:330px;top:176px;width:230px;text-align:center;font-family:var(--display);font-size:38px;line-height:38px;letter-spacing:1px}
  .hero-style{left:330px;top:202px;width:230px;text-align:center;font-family:var(--display);font-size:165px;line-height:165px;letter-spacing:2px}
  .hero-rule{position:absolute;left:369px;width:153px;height:1px;background:var(--white)}
  .hero-rule.first{top:348px}
  .hero-rule.second{top:352px}
  .hero-tagline{left:330px;top:373px;width:230px;text-align:center;font-family:var(--script);font-size:21px;line-height:28px}
  .spec-row{position:absolute;left:330px;top:417px;width:230px;display:flex;justify-content:center;font-family:var(--display);font-size:10.5px;letter-spacing:1.2px;line-height:11px;text-align:center}
  .spec-row span{padding:0 9px;border-left:1px solid var(--white)}
  .spec-row span:first-child{border-left:none}

  .refund-value{left:589px;top:252px;font-family:var(--sans);font-weight:500;font-size:18px;line-height:22px}
  .refund-terms{left:623px;top:254px;width:82px;white-space:normal !important;font-family:var(--sans);font-size:5.5px;line-height:7px;text-transform:uppercase}

  .std-drinks-label{left:600px;top:420px;transform:rotate(-90deg);transform-origin:left top;font-family:var(--sans);font-weight:500;font-size:14px;line-height:20px;width:120px;text-align:center}
  .std-glass{position:absolute;left:633px;top:300px;width:60px;height:128px}
  .std-value{left:633px;top:318px;width:60px;text-align:center;font-family:var(--sans);font-weight:500;font-size:18px;line-height:24px;color:var(--purple)}
  .volume{left:633px;top:429px;width:60px;text-align:center;font-family:var(--sans);font-size:12px;line-height:16px}

  .compliance-icon{position:absolute;top:207px;width:60px;height:60px}
  .icon-recycle{left:705px}
  .icon-pregnancy{left:774px}
</style>
</head>
<body>
<div class="canvas">
  <div class="can-label">
    <div class="header-band"></div>
    <svg class="wave" viewBox="0 0 888 462" aria-hidden="true">
      <path fill="#b7a5cd" d="M0 150 q7.5 -7 15 0 t15 0 t15 0 t15 0 t15 0 t15 0 t15 0 t15 0 t15 0 t15 0 t15 0 t15 0 t15 0 t15 0 t15 0 t15 0 t15 0 t15 0 t15 0 t15 0 t15 0 t15 0 t15 0 t15 0 t15 0 t15 0 t15 0 t15 0 t15 0 t15 0 t15 0 t15 0 t15 0 t15 0 t15 0 t15 0 t15 0 t15 0 t15 0 t15 0 t15 0 t15 0 t15 0 t15 0 t15 0 t15 0 t15 0 t15 0 t15 0 t15 0 t15 0 t15 0 t15 0 t15 0 t15 0 t15 0 t15 0 t15 0 t15 0 t15 0 t15 0 L888 462 L0 462 Z"/>
    </svg>

    <p class="tagline-header">Socially Approachable</p>
    <p class="brand-name">CALLOWAY<br>BREWHOUSE</p>
    <div class="origin-stamp"></div>

    <h2 class="side-title">WENDEL MALT IPA</h2>
    <div class="side-rule"></div>
    <p class="tasting-notes">BRIGHT IN COLOUR, DRY ON THE PALATE AND THIRST QUENCHING IN THE EXTREME, WHEAT AND PALE MALTS COMPLIMENT EACH OTHER WITH NUANCE</p>
    <div class="member-badge"></div>
    <p class="brewed-at">Brewed &amp; canned<br>10 Harbour Lane Seaford</p>
    <p class="made-in">MADE IN AUSTRALIA</p>
    <p class="side-abv">4.8% ABV</p>

    <h1 class="hero-name">WENDEL MALT</h1>
    <p class="hero-style">IPA</p>
    <div class="hero-rule first"></div>
    <div class="hero-rule second"></div>
    <p class="hero-tagline">Socially Approachable</p>
    <div class="spec-row">
      <span>4.8%<br>ABV</span>
      <span>AUSTRALIAN<br>CRAFTED</span>
      <span>330<br>ML</span>
    </div>

    <svg class="compliance-icon icon-recycle" viewBox="0 0 60 60" aria-hidden="true">
      <circle cx="30" cy="30" r="26" fill="none" stroke="#ffffff" stroke-width="3"/>
    </svg>
    <svg class="compliance-icon icon-pregnancy" viewBox="0 0 60 60" aria-hidden="true">
      <circle cx="30" cy="30" r="26" fill="none" stroke="#ffffff" stroke-width="3"/>
      <line x1="12" y1="12" x2="48" y2="48" stroke="#ffffff" stroke-width="3"/>
    </svg>

    <p class="refund-value">10c</p>
    <p class="refund-terms">Refund at collection depots in state of purchase</p>

    <p class="std-drinks-label">Standard Drinks</p>
    <svg class="std-glass" viewBox="0 0 60 128" aria-hidden="true">
      <path d="M2 2 H58 L51 126 H9 Z" fill="#ffffff"/>
    </svg>
    <p class="std-value">1.2</p>
    <p class="volume">330ml</p>
  </div>

  <div class="bleed-top"></div>
  <div class="bleed-bottom"></div>
  <div class="bleed-guide" style="left:150px"></div>
  <div class="bleed-guide" style="left:174px"></div>
  <div class="bleed-guide" style="left:1015px"></div>
  <div class="bleed-guide" style="left:1038px"></div>
</div>
</body>
</html>
```